Premium Label Design for Sleep Supplement Targeted at Shift Workers (Vendora Launch)

🧠 PROJECT OVERVIEW

We are launching a premium dietary supplement brand on Vendora called:

Lumen Crestworks

The product is:

DuskaHush – Shift Work Sleep & Recovery Formula

This supplement is specifically designed for shift workers (nurses, emergency responders, aviation crew, rotating schedule professionals) who struggle with irregular sleep cycles.

This is NOT a generic sleep supplement.
It is a targeted recovery solution.

The label must feel:

• Premium
• Modern
• Professional
• Performance-oriented
• Clean
• Vendora-ready

No clutter. No generic wellness design.

🎯 TARGET AUDIENCE

Primary:
Shift workers aged 25–55

Examples:
• Nurses
• Paramedics
• Aviation crew
• FIFO workers
• Rotating schedule professionals

These are responsible professionals.
The design must reflect trust and authority.

📦 PRODUCT DETAILS (FRONT LABEL ONLY)

Bottle Colour:
White plastic bottle

Label Type:
Wrap-around label

Primary Front Text (Hierarchy Matters):

1️⃣ Lumen Crestworks Logo
2️⃣ DuskaHush (moon crescent icon incorporated on the letter "g", if possible. This is desirable as it makes the text look unique.
3️⃣ Shift Work Sleep Support Formula
4️⃣ Also ideal for travel & irregular schedules -
Supports Circadian Rhythm, Restorative Sleep and Recovery*
5️⃣ 60 Capsules | 30-Day Supply

Include a small badge that reads:

Recommended by (plain badge shape) Professionals (badge icon or text). Icon preferably, on the top corner of the bottle or anywhere it can be noticed.

🎨 DESIGN DIRECTION (VERY IMPORTANT)

The design should feel:

Premium Performance Recovery
Modern Minimalist
Night-Aligned
Structured

Primary colour direction:

Deep midnight navy gradient
Top: #142A4A
Bottom: #081428

or a colour of your choice

Accent colours should be minimal.

Avoid bright green, neon, pastel, or spa-like tones.

❌ WHAT WE DO NOT WANT

No:
• Cheap private-label look
• Too much white

This must look like a serious modern supplement brand.

🧱 LAYOUT PREFERENCES

Strong top section with dark gradient band.

Product name (DuskaHush) must dominate.

Brand (Lumen Crestworks) must be present but secondary.

Shift Work Sleep Support Formula must be clear and confident.

Use white space intentionally.

Typography should be clean, modern sans-serif.

📐 VENDORA CONSIDERATIONS

The label must:

• Be readable at thumbnail size
• Have clear text hierarchy
• Not look cluttered
• Stand out in a crowded sleep supplement category
• Feel more premium than competitors

🏆 WINNING DESIGN WILL BE

• Modern and confident
• Clearly targeted
• Minimal but strong
• Professional
• Scalable to future products

📁 FILE REQUIREMENTS

Final files must include:

• AI or vector source files
• High-resolution print-ready files
• Editable files
• Font details

- Label Template is attached - this is supplied by the manufacturer to edit. Modify it in any way you like to suit the design style.

- Certificates are attached and can be modified to suit label design theme ( I require all three certificates to be displayed - if you have better quality stock vector icons for the certificates please use those as you desire, but they must be placed. Doesn't have to be exactly as the ones I have supplied. They don't have to be on the front label either.

- Stock vector icons for - NON-GMO or GMO Free, No Artificial Additives, Non-Habit Forming and Herbal Extract Blend - must be included - it doesn't have to be on the front label though.

- Lumen Crestworks Logo is Provided.

On Supplement Fact Label Section, please include -
Manufactured for and distributed by:
LUMEN CRESTWORKS - USE TEXT LOGO PROVIDED
4718 Harbor Vale Road, Suite 112 PMB 947
Dallas, TX 75019 United States

-UPC code needs to be placed on label. It can be altered to suit label. Use the guidelines on this website ;
https://help.codemintery.example/en/guides/articles/49000037215-resizing-your-barcode-artwork

LUMEN CRESTWORKS Logo font is Open Sans Light LUMEN is in Bold.

Ideally, I would like some white stars on the label.

I have attached some specific things I like so far from the submissions to the brief -please try to incorporate these as closely as possible.

-----UPDATE-----

Thank you all for your submissions.

I have come up with a sample design using AI and this is what I want you to work with as an example. The image we just generated is a raster mockup (PNG).
It is not a true vector file, so it cannot simply be converted into a clean professional Illustrator (.AI) file without rebuilding it properly. Please rebuild the entire 6" x 2.5" label as:

• True vector layout
• Fully editable
• Proper CMYK setup
• 300 DPI
• 0.125" bleed
• Correct safe margins
• Separate layers
• Editable text (Open Sans family)
• Vector icons
• Proper Supplement Facts formatting

That means I will get a real production-ready Illustrator file, not a traced image. The designer who can produce this will be the winner. Please note, icons are not correct. This is for visual guidance only. Please follow all instructions as per the brief provided. I look forward to your submissions and working with you on this project.

Target Market(s)

Shift Workers who are willing to pay a premium for a sleep aid/supplement

Industry/Entity Type

• Nurses • Paramedics • Aviation crew • FIFO workers • Rotating schedule professionals

Colors

Designer to choose colors to be used in the design.

Requirements
Must have
• As per brief - icons (NON-GMO or GMO Free, No Artificial Additives, Non-Habit Forming and Herbal Extract Blend), stars, moon image incorporated onto the "g" letter of DuskaHush (image attached for ideas), recommended by (plain badge shape) Crew (preferably an Icon), Certificates (uploaded) can be customised to suit label from your own vectors.
Nice to have
• As per brief
Should not have
• As per brief

```html
<!DOCTYPE html>
<html lang="en">
<head>
<meta charset="utf-8">
<title>DuskaHush – Shift Work Sleep Support Formula Label</title>
<link href="https://fonts.googleapis.com/css2?family=Nunito:wght@800;900&family=Open+Sans:wght@300;400;600;700;800&display=swap" rel="stylesheet">
<style>
  :root{
    --page:#e8e8eb;
    --navy-deep:#0a1030;
    --navy:#151c52;
    --indigo:#2b2f86;
    --violet:#5a3fb8;
    --magenta:#e23fd6;
    --pink:#f6b8f0;
    --silver-hi:#f4f5f7;
    --silver:#c9ccd3;
    --silver-lo:#9ea3ad;
    --ink:#1c1f3a;
    --white:#ffffff;
    --mist:rgba(220,222,232,.55);
  }
  *{box-sizing:border-box;margin:0;padding:0}
  html,body{width:1200px;height:1200px;overflow:hidden}
  body{background:var(--page);font-family:"Open Sans",Arial,sans-serif;color:var(--white);position:relative}

  .label{position:absolute;left:20px;top:290px;width:1160px;height:620px;display:flex;overflow:hidden;border-radius:4px}
  .panel{position:relative;height:100%;overflow:hidden}
  .panel--facts{width:330px}
  .panel--front{width:500px}
  .panel--trust{width:330px}

  .night-sky{position:absolute;inset:0;
    background:
      radial-gradient(ellipse 70% 18% at 50% 70%, rgba(226,63,214,.45), transparent 70%),
      radial-gradient(ellipse 60% 40% at 60% 40%, rgba(90,63,184,.55), transparent 75%),
      linear-gradient(180deg, var(--silver) 0%, var(--navy-deep) 14%, var(--navy) 40%, var(--indigo) 62%, var(--mist) 82%, var(--silver) 100%);}
  .panel--front .night-sky{background:
      radial-gradient(ellipse 70% 14% at 45% 68%, rgba(226,63,214,.6), transparent 70%),
      radial-gradient(ellipse 50% 35% at 75% 45%, rgba(120,110,220,.55), transparent 75%),
      linear-gradient(180deg, var(--navy-deep) 0%, var(--navy) 35%, var(--indigo) 60%, #8a8fb0 80%, var(--silver) 100%);}

  /* front panel */
  .top-band{position:absolute;left:150px;top:0;right:0;height:66px;border-bottom-left-radius:26px;
    background:linear-gradient(180deg,var(--silver-hi),var(--silver));}
  .brand{position:absolute;right:22px;top:22px;display:flex;align-items:center;gap:8px;
    font-weight:400;font-size:17px;letter-spacing:.5px;color:var(--ink)}
  .brand__dot{width:24px;height:24px;border-radius:50%;background:var(--violet)}
  .crew-badge{position:absolute;left:86px;top:26px;width:100px;height:108px}
  .product-name{position:absolute;left:44px;top:150px;font-family:"Nunito",Arial,sans-serif;font-weight:900;line-height:1}
  .product-name__top{display:block;font-size:62px;
    background:linear-gradient(180deg,var(--white) 30%,#7fb6ff);-webkit-background-clip:text;background-clip:text;color:transparent}
  .product-name__main{display:block;font-size:128px;margin-top:-4px;letter-spacing:-2px;
    background:linear-gradient(180deg,var(--white) 10%,var(--pink) 45%,var(--magenta) 90%);-webkit-background-clip:text;background-clip:text;color:transparent}
  .formula{position:absolute;left:52px;top:375px;font-size:22px;font-weight:400;letter-spacing:.3px}
  .formula-rule{position:absolute;left:52px;top:412px;width:370px;height:1px;background:rgba(255,255,255,.6)}
  .benefits{position:absolute;left:48px;top:443px;font-size:13.5px;font-weight:800;line-height:1.2}
  .travel-pill{position:absolute;left:236px;top:442px;width:190px;height:38px;padding:5px 14px;
    background:rgba(235,236,242,.9);border-top-right-radius:16px;border-bottom-right-radius:16px;
    color:#4a4d63;font-size:11px;font-weight:300;line-height:1.2}
  .claims{position:absolute;left:40px;top:514px;display:flex;gap:12px}
  .claim{width:54px;text-align:center;color:var(--ink);font-size:7px;font-weight:800;line-height:1.15}
  .claim__icon{width:50px;height:50px;border-radius:50%;margin:0 auto 10px;border:3px solid var(--silver-hi);
    background:var(--indigo);box-shadow:0 0 0 1px var(--silver-lo)}
  .claim__icon--light{background:var(--white)}
  .claim__icon svg{width:100%;height:100%}
  .count-box{position:absolute;left:362px;top:528px;width:114px;height:76px;border-radius:18px 0 0 0;
    background:linear-gradient(180deg,var(--silver-hi),var(--silver));color:var(--ink);text-align:center;padding-top:12px;font-size:12px;line-height:1.3}
  .count-box strong{font-weight:700}
  .supplement-tag{position:absolute;left:0;right:0;bottom:0;height:16px;background:var(--magenta);color:var(--white);font-size:7.5px;line-height:16px;letter-spacing:.3px}

  /* facts panel */
  .facts{position:absolute;left:44px;top:96px;width:300px;height:318px;border:1px solid rgba(255,255,255,.5);border-radius:14px;
    background:rgba(210,212,222,.55);padding:22px 0 0 34px;color:var(--white)}
  .facts__title{font-size:22px;font-weight:600}
  .facts__serving{font-size:10.5px;font-weight:300;margin-top:6px;line-height:1.35}
  .facts__rule{height:2px;background:var(--white);margin:10px 0 0;width:250px}
  .facts__head{font-size:6px;text-align:right;padding-right:2px;font-weight:700;margin-top:16px}
  .facts__row{border-top:1px solid rgba(255,255,255,.55);padding:10px 0 10px;font-size:7px;line-height:1.3;width:260px}
  .facts__row b{font-weight:700;display:block}
  .facts__row span{font-weight:300}
  .facts-notes{position:absolute;left:44px;top:440px;width:270px;font-size:8.5px;line-height:1.35}
  .facts-notes b{font-weight:700}
  .facts-notes p{margin-bottom:10px}

  /* trust panel */
  .seals{position:absolute;left:44px;top:78px;display:grid;grid-template-columns:110px 110px;column-gap:38px;row-gap:14px}
  .seal{text-align:center;font-size:9px;font-weight:700;line-height:1.2}
  .seal__disc{width:86px;height:86px;border-radius:50%;margin:0 auto 8px;border:4px solid var(--silver-hi);box-shadow:0 0 0 1px var(--silver-lo)}
  .seal__disc--light{background:var(--white)}
  .seal__disc--dark{background:var(--indigo)}
  .seal__disc svg{width:100%;height:100%}
  .distributor{position:absolute;left:0;right:0;top:458px;text-align:center;font-size:10.5px;line-height:1.4}
  .distributor b{font-weight:700}
  .distributor__address{font-weight:300;margin-top:8px;font-size:10px}
</style>
</head>
<body>
<main class="label">

  <!-- Supplement facts panel -->
  <section class="panel panel--facts">
    <div class="night-sky" role="img" aria-label="Starry night sky fading to silver mist"></div>
    <div class="facts">
      <h2 class="facts__title">Supplement Facts</h2>
      <p class="facts__serving">Serving Size: 2 Capsules<br>Servings Per Container: 30</p>
      <div class="facts__rule"></div>
      <p class="facts__head">Amount</p>
      <div class="facts__row"><b>Vitamin B6</b><span>(Daily Ext ACC) / (Pyridoxine HCl)</span></div>
      <div class="facts__row"><b>Vitamin B6</b><span>(Daily Ext ACC) / (Pyridoxine HCl)</span></div>
      <div class="facts__row"><b>Vitamin B6</b><span>(Daily Ext ACC) / (Pyridoxine HCl)</span></div>
      <div class="facts__row"><b>Vitamin B6</b><span>(Daily Ext ACC) / (Pyridoxine HCl)</span></div>
      <div class="facts__row"><b>Vitamin B6</b><span>(Daily Ext ACC) / (Pyridoxine HCl)</span></div>
    </div>
    <div class="facts-notes">
      <p><b>Daily Value (DV) not established**</b><br><b>Other ingredients: Vegetable cellulose capsule, rice flour, magnesium stearate.</b></p>
      <p><b>SUGGESTED USE:</b><br>Take 2 capsules 30 minutes before bedtime or as directed by your healthcare professional.</p>
      <p><b>WARNING:</b><br>Do not use if pregnant, nursing, under 18, or taking medication without consulting a healthcare professional. May cause drowsiness. Store in a cool, dry place.</p>
    </div>
  </section>

  <!-- Front panel -->
  <section class="panel panel--front">
    <div class="night-sky" role="img" aria-label="Starry night sky with violet glow over a misty mountain horizon"></div>
    <div class="top-band"></div>
    <div class="brand"><span class="brand__dot"></span><span>LUMEN CRESTWORKS</span></div>
    <svg class="crew-badge" viewBox="0 0 100 108" aria-hidden="true">
      <path d="M50 2 L96 14 V56 C96 82 74 98 50 106 C26 98 4 82 4 56 V14 Z" fill="#e9eaef" stroke="#9ea3ad" stroke-width="3"/>
      <path d="M50 12 L86 21 V56 C86 76 70 89 50 96 C30 89 14 76 14 56 V21 Z" fill="#cfd2da"/>
    </svg>
    <h1 class="product-name"><span class="product-name__top">Duska</span><span class="product-name__main">Hush</span></h1>
    <p class="formula">Shift work sleep Support formula</p>
    <div class="formula-rule"></div>
    <p class="benefits">Supports Circadian Rhythm<br>Restoreative Sleep</p>
    <p class="travel-pill">Also ideal for travel &amp; irregular schedules</p>
    <div class="claims">
      <div class="claim"><div class="claim__icon claim__icon--light"><svg viewBox="0 0 50 50"><circle cx="22" cy="22" r="13" fill="none" stroke="#1c1f3a" stroke-width="2"/><line x1="13" y1="13" x2="31" y2="31" stroke="#1c1f3a" stroke-width="2"/></svg></div>NON-GMO</div>
      <div class="claim"><div class="claim__icon"><svg viewBox="0 0 50 50"><rect x="15" y="14" width="14" height="18" rx="2" fill="none" stroke="#fff" stroke-width="1.6"/><rect x="17" y="10" width="10" height="4" fill="#fff"/></svg></div>NO ARTIFICIAL ADDITIVES</div>
      <div class="claim"><div class="claim__icon"><svg viewBox="0 0 50 50"><circle cx="22" cy="22" r="8" fill="none" stroke="#fff" stroke-width="1.6"/><path d="M14 30 L8 36" stroke="#fff" stroke-width="1.6"/></svg></div>NON-HABIT FORMING</div>
      <div class="claim"><div class="claim__icon"><svg viewBox="0 0 50 50"><path d="M12 24 H32 C32 31 27 34 22 34 C17 34 12 31 12 24 Z" fill="none" stroke="#fff" stroke-width="1.6"/><path d="M22 24 V12" stroke="#fff" stroke-width="1.6"/></svg></div>HERBAL EXTRACT BLEND.</div>
    </div>
    <div class="count-box">
      <strong>60</strong> Capsules<br>30-Day Supply
      <div class="supplement-tag">DIETARY SUPPLEMENT</div>
    </div>
  </section>

  <!-- Trust panel -->
  <section class="panel panel--trust">
    <div class="night-sky" role="img" aria-label="Starry night sky fading to silver mist"></div>
    <div class="seals">
      <div class="seal"><div class="seal__disc seal__disc--light"><svg viewBox="0 0 86 86"><circle cx="39" cy="39" r="22" fill="none" stroke="#1c1f3a" stroke-width="2"/><line x1="24" y1="24" x2="54" y2="54" stroke="#1c1f3a" stroke-width="2"/></svg></div>NON-GMO</div>
      <div class="seal"><div class="seal__disc seal__disc--dark"><svg viewBox="0 0 86 86"><rect x="28" y="26" width="22" height="28" rx="3" fill="none" stroke="#fff" stroke-width="2"/><rect x="31" y="20" width="16" height="6" fill="#fff"/></svg></div>NO ARTIFICIAL ADDITIVES</div>
      <div class="seal"><div class="seal__disc seal__disc--light"></div></div>
      <div class="seal"><div class="seal__disc seal__disc--dark"></div></div>
      <div class="seal"><div class="seal__disc seal__disc--light"></div></div>
      <div class="seal"><div class="seal__disc seal__disc--dark"></div></div>
    </div>
    <div class="distributor">
      <p><b>Manufactured for and distributed by:<br>LUMEN CRESTWORKS</b></p>
      <p class="distributor__address">4718 Harbor Vale Road, Suite 112 PMB 947<br>Dallas, TX 75019 United States<br>www.lumencrestworks.example | support@lumencrestworks.example</p>
    </div>
  </section>

</main>
</body>
</html>
```